4x6 postcard design Tide And Time

A full color double sided postcard 4x6 postcard. I have attached a screenshot of the text that should be used on the postcard. The front is titled this is the front. The back is titled the back. REMEMBER THE screenshots are used to show you the text. Please design using your own creative methods. The color scheme should remain pretty similar to the screenshot.

On the front of the card, I'd like to add a 4th bullet (or check) that says This is NOT cash gifting!
Also on the front, add a line that says call 877-402-3915 or send an email to join@tideandtimeco.net and mention ID#:

On the back, please add a line that says call 877-402-3915 or send an email to join@tideandtimeco.net and mention ID#:

On the front OR back it should say 100% Satisfaction Guarantee

Target Market(s)

work from home

Font styles to use
Sans Serif

Requirements
Must have
• The correct text on both sides. Please read the directions carefully.
Nice to have
• A very creative, attention-grabbing design. The 100% Satisfaction Guarantee designed in a way that looks like the gold seals that pop up if you google "money back guarantee seal"

```html
<!DOCTYPE html>
<html lang="en">
<head>
<meta charset="utf-8">
<title>Tide And Time – Postcard</title>
<link href="https://fonts.googleapis.com/css2?family=Oswald:wght@400;500;600;700&family=Pathway+Gothic+One&family=Montserrat:wght@400;700&family=Sacramento&display=swap" rel="stylesheet">
<style>
  :root{
    --green:#0f8c4a;
    --gold:#e5ac2b;
    --ink:#1d1d1d;
    --grey:#dcdddc;
    --white:#ffffff;
    --page:#ececea;
  }
  *{box-sizing:border-box;margin:0;padding:0}
  html,body{width:869px;height:1200px;overflow:hidden;background:var(--page)}
  body{position:relative;font-family:"Pathway Gothic One",sans-serif;color:var(--ink)}
  .card{position:absolute;left:67px;width:734px;height:489px;background:var(--white);overflow:hidden;box-shadow:0 4px 14px rgba(0,0,0,.18)}
  .card--front{top:55px}
  .card--back{top:664px}
  .abs{position:absolute}

  /* front */
  .brand{left:22px;top:74px;display:flex;align-items:center;gap:8px}
  .brand__dot{width:22px;height:22px;border-radius:50%;background:var(--gold)}
  .brand__name{font-family:"Oswald",sans-serif;font-weight:600;font-size:21px;color:var(--green);white-space:nowrap}
  .photo{left:150px;top:14px;width:250px;height:350px;background:radial-gradient(ellipse at 55% 45%,#cfcfd2 0%,#e8e6e4 45%,#ffffff 75%)}
  .band{left:0;top:0}
  .call-label{left:60px;top:384px;width:296px;display:flex;align-items:center;gap:8px;color:var(--white);font-family:"Oswald",sans-serif;font-size:19px;white-space:nowrap}
  .call-label::before,.call-label::after{content:"";flex:1;height:1px;background:rgba(255,255,255,.7)}
  .phone{left:52px;top:404px;display:flex;align-items:center;gap:10px}
  .phone__num{font-family:"Oswald",sans-serif;font-weight:600;font-size:46px;letter-spacing:3px;color:var(--white);line-height:1}
  .mail-line{left:57px;top:458px;font-size:13px;color:var(--white);white-space:nowrap;display:flex;align-items:center;gap:4px}
  .mail-line b{color:var(--gold);font-weight:400}
  .id-box{display:inline-block;width:58px;height:12px;background:var(--white)}
  .headline-1{left:430px;top:18px;font-family:"Oswald",sans-serif;font-weight:700;font-size:82px;line-height:1;color:var(--green);letter-spacing:-1px}
  .headline-2{left:430px;top:98px;font-family:"Oswald",sans-serif;font-weight:700;font-size:50px;line-height:1;color:var(--gold);letter-spacing:-1.5px;transform:scaleX(.84);transform-origin:left}
  .rule{left:428px;top:154px;width:282px;height:1px;background:var(--gold)}
  .intro{left:432px;top:160px;font-family:"Montserrat",sans-serif;font-size:13.5px;line-height:17px;white-space:nowrap}
  .script{left:550px;top:198px;font-family:"Sacramento",cursive;font-size:28px;line-height:1;color:var(--gold);white-space:nowrap}
  .rule-short{left:428px;top:216px;width:118px;height:1px;background:var(--gold)}
  .thousands{left:428px;top:230px;font-family:"Oswald",sans-serif;font-weight:700;font-size:46px;line-height:1;letter-spacing:1.5px;color:var(--gold)}
  .perks{left:421px;top:317px;width:313px;height:134px;border:2px solid var(--gold);border-right:none}
  .perks ul{list-style:none;position:absolute;left:28px;top:34px}
  .perks li{font-size:14px;line-height:23.5px;display:flex;align-items:center;gap:6px;white-space:nowrap}
  .perks strong{font-family:"Oswald",sans-serif;font-weight:700;font-size:12px;margin:0 -2px}
  .seal-tab{left:484px;top:297px;width:133px;height:41px;background:var(--gold);clip-path:polygon(0 0,100% 0,92% 100%,0 100%);color:var(--white);font-family:"Montserrat",sans-serif;font-weight:700;font-size:11.5px;line-height:12px;padding:8px 0 0 28px}
  .seal{left:425px;top:286px;width:60px;height:60px;border-radius:50%;background:var(--green);border:3px solid var(--white);color:var(--white);font-family:"Oswald",sans-serif;font-size:21px;display:flex;align-items:center;justify-content:center}
  .signup{right:9px;top:457px;font-family:"Oswald",sans-serif;font-weight:700;font-size:21px;color:var(--white);letter-spacing:-.5px}

  /* back */
  .back-panel{left:0;top:0;width:373px;height:489px;background:var(--grey)}
  .q-banner{left:0;top:29px;width:332px;height:43px;background:var(--gold);clip-path:polygon(0 0,100% 0,93% 100%,0 100%);color:var(--white);font-family:"Oswald",sans-serif;font-weight:600;font-size:20px;line-height:34px;letter-spacing:-.6px;padding:3px 0 0 28px;white-space:nowrap}
  .about{left:29px;top:84px;width:314px;font-size:15.5px;line-height:20.5px;text-align:justify}
  .about b{font-family:"Oswald",sans-serif;font-weight:500;font-size:14px}
  .steps{left:54px;top:186px;width:290px;list-style:none;font-size:15.5px;line-height:19px;counter-reset:s}
  .steps li{position:relative;padding-left:21px;margin-bottom:9px;counter-increment:s}
  .steps li::before{content:counter(s);position:absolute;left:0;top:3px;width:14px;height:14px;border-radius:50%;background:var(--gold);color:var(--white);font-family:"Oswald",sans-serif;font-size:9px;line-height:14px;text-align:center}
  .cash{left:31px;top:314px;width:310px;font-family:"Oswald",sans-serif;font-weight:500;font-size:13.5px;line-height:18px;letter-spacing:-.4px;white-space:nowrap}
  .black-bar{left:0;top:363px;width:373px;height:30px;background:#0c0c0c;color:var(--white);font-family:"Oswald",sans-serif;font-weight:500;font-size:15px;line-height:30px;padding-left:30px;letter-spacing:-.3px}
  .gold-block{left:0;top:393px;width:373px;height:96px;background:var(--gold);color:var(--white);font-family:"Oswald",sans-serif;font-size:15px;line-height:22px;padding:14px 0 0 30px;letter-spacing:-.3px}
  .gold-block .id-box{width:84px;height:14px;vertical-align:middle}
  .stamp{left:634px;top:33px;width:73px;height:73px;border:1.5px solid #6b6b6b}
  .addr-line{left:463px;width:244px;height:1.5px;background:#555}
</style>
</head>
<body>

<section class="card card--front">
  <div class="abs photo" role="img" aria-label="Photo of a young woman seated on a chair working on a laptop"></div>

  <div class="abs brand"><span class="brand__dot"></span><span class="brand__name">Tide And Time</span></div>

  <svg class="abs band" width="734" height="489" viewBox="0 0 734 489" aria-hidden="true">
    <path d="M0,376 Q210,354 423,362 L423,454 L734,454 L734,489 L0,489 Z" fill="var(--green)"/>
    <path d="M0,376 Q210,354 423,362" fill="none" stroke="var(--gold)" stroke-width="4"/>
  </svg>

  <div class="abs call-label">CALL US AT:</div>
  <div class="abs phone">
    <svg width="30" height="30" viewBox="0 0 24 24" aria-hidden="true">
      <path d="M6.6 10.8a15.5 15.5 0 0 0 6.6 6.6l2.2-2.2a1 1 0 0 1 1-.25 11.4 11.4 0 0 0 3.6.57 1 1 0 0 1 1 1V20a1 1 0 0 1-1 1A17 17 0 0 1 3 4a1 1 0 0 1 1-1h3.5a1 1 0 0 1 1 1c0 1.25.2 2.450.57 3.6a1 1 0 0 1-.25 1z" fill="var(--gold)"/>
      <path d="M14 3a7 7 0 0 1 7 7M14 6.5a3.5 3.5 0 0 1 3.5 3.5" fill="none" stroke="var(--gold)" stroke-width="1.6"/>
    </svg>
    <span class="phone__num">877-402-3915</span>
  </div>
  <div class="abs mail-line">or send an email to <b>join@tideandtimeco.net</b> and mention ID#: <span class="id-box"></span></div>

  <h1 class="abs headline-1">DON’T</h1>
  <h2 class="abs headline-2">PROCRASTINATE</h2>
  <div class="abs rule"></div>
  <p class="abs intro">People just like you are averaging over<br>$30,000 per month with our quick<br>and easy system.</p>
  <div class="abs rule-short"></div>
  <div class="abs script">Start Earning</div>
  <div class="abs thousands">THOUSANDS</div>

  <div class="abs perks">
    <ul>
      <li><svg width="10" height="10" viewBox="0 0 10 10" aria-hidden="true"><rect x=".5" y="2" width="7" height="7" fill="none" stroke="var(--gold)"/><path d="M2 5l2 2 5-6" fill="none" stroke="var(--gold)" stroke-width="1.2"/></svg>We close all your sales for you... Earn money 24 hours a day!</li>
      <li><svg width="10" height="10" viewBox="0 0 10 10" aria-hidden="true"><rect x=".5" y="2" width="7" height="7" fill="none" stroke="var(--gold)"/><path d="M2 5l2 2 5-6" fill="none" stroke="var(--gold)" stroke-width="1.2"/></svg>Done-for-you Marketing System</li>
      <li><svg width="10" height="10" viewBox="0 0 10 10" aria-hidden="true"><rect x=".5" y="2" width="7" height="7" fill="none" stroke="var(--gold)"/><path d="M2 5l2 2 5-6" fill="none" stroke="var(--gold)" stroke-width="1.2"/></svg>Real Products that pay “Gigantic” cash commisions!</li>
      <li><svg width="10" height="10" viewBox="0 0 10 10" aria-hidden="true"><rect x=".5" y="2" width="7" height="7" fill="none" stroke="var(--gold)"/><path d="M2 5l2 2 5-6" fill="none" stroke="var(--gold)" stroke-width="1.2"/></svg>This is <strong>NOT</strong> cash gifting!</li>
    </ul>
  </div>
  <div class="abs seal-tab">GUARANTEED<br>SATISFACTION</div>
  <div class="abs seal">100%</div>

  <div class="abs signup">SIGN UP NOW!</div>
</section>

<section class="card card--back">
  <div class="abs back-panel"></div>
  <h2 class="abs q-banner">What is a courseware distributor?</h2>
  <p class="abs about">A Courseware Distributor is someone such as yourself that joins <b>Tide And Time</b>, and earns thousands of dollars in cash commissions each week. All you have to do is follow 3 simple steps to change your financial health forever:</p>
  <ol class="abs steps">
    <li>Call or email right away to join</li>
    <li>Allow our attention-grabbing postcards or sales letters to work for you to get sales while you sleep.</li>
    <li>Sit back and let our trained professionals answer your calls and close your sales.</li>
  </ol>
  <p class="abs cash">Your CASH commision will arrive at your door via<br>Overnight Courier, 6 days per week.</p>
  <div class="abs black-bar">SIGN UP NOW! - 100% GUARANTEED SATISFACTION</div>
  <div class="abs gold-block">
    call 877-402-3915<br>
    or send an email to join@tideandtimeco.net<br>
    and mention ID#: <span class="id-box"></span>
  </div>

  <div class="abs stamp"></div>
  <div class="abs addr-line" style="top:192px"></div>
  <div class="abs addr-line" style="top:222px"></div>
  <div class="abs addr-line" style="top:251px"></div>
  <div class="abs addr-line" style="top:281px"></div>
</section>

</body>
</html>
```